LITTLE DESIGN WORK REQUIRED!

UPDATE: WE WEREN'T OVERLY ECSTATIC WITH THE DESIGNS WE WERE RECEIVING SO WE DID MOST OF THE DESIGN WORK OURSELVES...

PLEASE SEE THE NEWLY ATTACHED PPT DOC TO VIEW NEARLY EXACT REPLICAS OF WHAT WE WANT THE SITE TO LOOK LIKE. WE NOW NEED YOUR HELP TO MAKE IT LOOK LIKE SOMETHING WORTHY OF THE WEB.

NO CODING REQUIRED - EXPECTED OUTPUT PSD FILES

Hi everyone!

We're looking for a designer to work their magic for our site! We're a not-for-profit program aimed at helping young people realise their potential!

In the attached PPT file, you'll notice we've already DESIGNED THE ENTIRE SITE IN POWERPOINT. Now, we need YOU to make the small changes we requested in the document as well as design the whole thing in psd.

Any questions, don't hesitate to ask.

Brook-Rise
Updates

We've done about 95% of the design for you. Please fine-tune it. See the newly attached PPT doc for details. 

The best two designs will win. This project closes on Friday - please message us if you are absolutely sure you cannot make the deadline.

Thanks,
Brook-Rise

```html
<!DOCTYPE html>
<html lang="en">
<head>
<meta charset="utf-8">
<title>Brook-Rise</title>
<link rel="stylesheet" href="https://fonts.googleapis.com/css2?family=Arimo:wght@400;700&display=swap">
<style>
:root{
  --backdrop:#3d3d3d;
  --page:#ffffff;
  --ink:#333333;
  --muted:#555555;
  --nav:#3f3f3f;
  --green:#1fc51a;
  --leaf:#7cc242;
  --step:#eeeeee;
  --step-ink:#a6a6a6;
  --sky:#66c6d6;
  --teal:#7bbfae;
  --moss:#a8c97a;
  --tile:#f2f1f1;
  --footer:#f2f2f2;
  --rule:#e4e4e4;
  --hero-fill:#b4bfc6;
}
*{box-sizing:border-box;margin:0;padding:0}
html,body{width:853px;height:1200px;overflow:hidden}
body{background:var(--backdrop);font-family:"Arimo",Arial,sans-serif;color:var(--ink);position:relative}
.page{position:absolute;left:100px;top:53px;width:654px;height:1138px;background:var(--page)}
.abs{position:absolute}

/* header */
.brand{left:13px;top:22px;display:flex;align-items:center;gap:8px}
.brand-mark{width:26px;height:26px;background:var(--green)}
.brand-name{font-size:27px;font-weight:700;color:#222;letter-spacing:-0.5px}
.search{left:413px;top:31px;width:189px;height:25px;border:1px solid #d8d8d8;border-radius:3px;box-shadow:inset 0 1px 2px rgba(0,0,0,.08);font-size:8px;color:#b0b0b0;padding:8px 8px}
.search-btn{left:601px;top:31px;width:31px;height:25px;background:#3c3c3c;border-radius:3px}

/* nav */
.nav{left:13px;top:79px;width:625px;height:46px;background:var(--nav);display:flex;list-style:none}
.nav li{width:100px;color:#fff;font-size:10px;display:flex;align-items:center;justify-content:center}
.nav li.active{width:115px;background:var(--green)}

/* hero */
.hero-photo{left:13px;top:126px;width:418px;height:206px;background:linear-gradient(180deg,#c2ccd3,#a9b3b8);border:1px solid #9aa}
.hero-panel{left:433px;top:126px;width:207px;height:206px;background:var(--green);border:1px solid #6ad867}
.hero-title{position:absolute;top:12px;width:100%;text-align:center;color:#fff;font-size:31px;font-weight:700}
.hero-icon{position:absolute;left:70px;top:58px;width:70px;height:66px;background:#dfe5ea;border-radius:6px}
.hero-cta{position:absolute;left:22px;top:136px;width:166px;height:49px;background:linear-gradient(180deg,#27a32a,#127a17);border:2px solid #b9efb6;box-shadow:0 0 4px rgba(255,255,255,.6);color:#fff;font-size:15.5px;line-height:19px;text-align:center;padding-top:5px}
.dots{left:23px;top:339px;display:flex;gap:4px}
.dots span{width:18px;height:18px;border-radius:50%;background:#6fb33c}
.dots span.current{background:#c8c8c8}
.rule{left:13px;top:363px;width:627px;height:1px;background:var(--rule)}

/* intro */
.intro{left:25px;top:377px;width:410px;font-size:7.6px;line-height:9.5px;color:var(--muted)}
.intro p{margin-bottom:7px}
.intro b{color:#222}
.steps{left:26px;top:442px}
.steps text{font-family:"Arimo",Arial,sans-serif;font-size:11px}

/* posts */
.posts-title{left:27px;top:503px;font-size:16px;font-weight:400;color:#333}
.category{left:27px;top:529px;width:383px;height:18px;background:linear-gradient(180deg,#9fd86a,#6cc134);color:#fff;font-size:12px;padding:2px 5px}
.post{left:29px;width:385px;height:94px}
.post-title{font-size:9px;color:#333}
.post-thumb{position:absolute;left:0;top:15px;width:81px;height:62px;background:var(--tile);border:1px solid #dedede;font-size:9px;color:#666;display:flex;align-items:center;justify-content:center}
.post-body{position:absolute;left:88px;top:14px;width:300px;font-size:7.2px;line-height:11.9px;color:#444}

/* sidebar */
.card{left:452px;width:178px;height:156px;border:1px solid rgba(0,0,0,.08)}
.card::before{content:"";position:absolute;left:0;top:0;width:100%;height:10px;background:#eef4f4}
.card::after{content:"";position:absolute;left:12px;top:10px;border:7px solid transparent;border-top-color:#eef4f4}
.card h3{position:absolute;left:14px;top:24px;color:#fff;font-size:19px;font-weight:400;text-shadow:0 1px 2px rgba(0,0,0,.2)}
.card-touch{top:376px;background:var(--sky)}
.touch-art{position:absolute;left:36px;top:50px;width:110px;height:100px;background:#dfe5ea;border-radius:3px}
.card-popular{top:548px;background:var(--teal)}
.rank{position:absolute;left:16px;width:34px;height:31px;background:#fff;border:1px solid #cfe3dd;color:#2a7f6a;font-size:15px;display:flex;align-items:center;justify-content:center}
.rank-info{position:absolute;left:57px;color:#fff;font-size:7.6px;font-weight:700;line-height:18px}
.card-ambassadors{top:721px;background:var(--moss)}
.avatar{position:absolute;left:16px;width:34px;height:31px;background:#fff;border:1px solid #dde}
.avatar::after{content:"";position:absolute;left:8px;top:6px;width:16px;height:20px;background:#d3d3d3;border-radius:8px 8px 2px 2px}
.person{position:absolute;left:57px;color:#fff;font-size:7.6px;line-height:12px;font-weight:700}
.person i{display:block}
.more{position:absolute;left:20px;top:139px;color:#fff;font-size:7.6px;font-weight:700}

/* footer */
.footer{left:0;top:1071px;width:654px;height:67px;background:var(--footer);font-size:7.3px;color:#333}
.footer .copy{position:absolute;left:17px;top:35px}
.footer .contact{position:absolute;right:17px;top:31px}
</style>
</head>
<body>
<div class="page">
  <div class="abs brand"><span class="brand-mark"></span><span class="brand-name">BROOK-RISE</span></div>
  <div class="abs search">Enter Keyword</div>
  <div class="abs search-btn">
    <svg width="31" height="25" viewBox="0 0 31 25"><circle cx="14" cy="11" r="5" fill="none" stroke="#fff" stroke-width="2"/><line x1="18" y1="15" x2="22" y2="19" stroke="#fff" stroke-width="2.4" stroke-linecap="round"/></svg>
  </div>

  <ul class="abs nav">
    <li class="active">About Us</li><li>Resources</li><li>Workshops</li><li>Ambassadors</li><li>Feats</li>
  </ul>

  <div class="abs hero-photo" role="img" aria-label="Feature photograph for the Kilimanjaro feat"></div>
  <div class="abs hero-panel">
    <div class="hero-title">Kilimanjaro</div>
    <div class="hero-icon" role="img" aria-label="Illustration of a sign-up form"></div>
    <div class="hero-cta">Sign-up for our<br>Brook-Rise Feats.</div>
  </div>
  <div class="abs dots"><span class="current"></span><span></span><span></span><span></span></div>
  <div class="abs rule"></div>

  <div class="abs intro">
    <p><b>Brook-Rise</b> is a not-for-profit program aimed at helping people – especially young people – realise their potential and achieve success.</p>
    <p><b>Our resources</b> are categorised into four areas: discovery, design, build, and achieve – what we believe are the four steps in the achievement framework we teach.</p>
  </div>

  <svg class="abs steps" width="390" height="52" viewBox="0 0 390 52">
    <polygon points="0,0 92,0 105,26 92,51 0,51" fill="#eeeeee"/>
    <polygon points="93,0 186,0 199,26 186,51 93,51 106,26" fill="#7cc242"/>
    <polygon points="187,0 280,0 293,26 280,51 187,51 200,26" fill="#eeeeee"/>
    <polygon points="281,0 374,0 387,26 374,51 281,51 294,26" fill="#eeeeee"/>
    <text x="50" y="30" text-anchor="middle" fill="#a6a6a6">Discover</text>
    <text x="146" y="30" text-anchor="middle" fill="#fff">Design</text>
    <text x="241" y="30" text-anchor="middle" fill="#a6a6a6">Build</text>
    <text x="335" y="30" text-anchor="middle" fill="#a6a6a6">Achieve</text>
  </svg>

  <h2 class="abs posts-title">Recent Posts</h2>
  <div class="abs category">Design</div>

  <article class="abs post" style="top:557px"><div class="post-title">Title A</div><div class="post-thumb">Picture A</div><p class="post-body">Lorem ipsum dosectetur adipisicing elit, sed do. Lorem ipsum dosectetur adipisicing elit, sed do. Lorem ipsum dosectetur adipisicing elit, sed do. Lorem ipsum dosectetur adipisicing elit, sed do. Lorem ipsum dosectetur adipisicing elit, sed do. Lorem ipsum dosectetur adipisicing elit, sed do. Lorem ipsum dosectetur adipisicing elit, sed do. Lorem ipsum dosectetur adipisicing elit, sed do. Lorem ipsum dosectetur adipisicing elit.</p></article>
  <article class="abs post" style="top:651px"><div class="post-title">Title B</div><div class="post-thumb">Picture B</div><p class="post-body">Lorem ipsum dosectetur adipisicing elit, sed do. Lorem ipsum dosectetur adipisicing elit, sed do. Lorem ipsum dosectetur adipisicing elit, sed do. Lorem ipsum dosectetur adipisicing elit, sed do. Lorem ipsum dosectetur adipisicing elit, sed do. Lorem ipsum dosectetur adipisicing elit, sed do. Lorem ipsum dosectetur adipisicing elit, sed do. Lorem ipsum dosectetur adipisicing elit, sed do. Lorem ipsum dosectetur adipisicing elit.</p></article>
  <article class="abs post" style="top:746px"><div class="post-title">Title C</div><div class="post-thumb">Picture C</div><p class="post-body">Lorem ipsum dosectetur adipisicing elit, sed do. Lorem ipsum dosectetur adipisicing elit, sed do. Lorem ipsum dosectetur adipisicing elit, sed do. Lorem ipsum dosectetur adipisicing elit, sed do. Lorem ipsum dosectetur adipisicing elit, sed do. Lorem ipsum dosectetur adipisicing elit, sed do. Lorem ipsum dosectetur adipisicing elit, sed do. Lorem ipsum dosectetur adipisicing elit, sed do. Lorem ipsum dosectetur adipisicing elit.</p></article>
  <article class="abs post" style="top:839px"><div class="post-title">Title D</div><div class="post-thumb">Picture D</div><p class="post-body">Lorem ipsum dosectetur adipisicing elit, sed do. Lorem ipsum dosectetur adipisicing elit, sed do. Lorem ipsum dosectetur adipisicing elit, sed do. Lorem ipsum dosectetur adipisicing elit, sed do. Lorem ipsum dosectetur adipisicing elit, sed do. Lorem ipsum dosectetur adipisicing elit, sed do. Lorem ipsum dosectetur adipisicing elit, sed do. Lorem ipsum dosectetur adipisicing elit, sed do. Lorem ipsum dosectetur adipisicing elit.</p></article>
  <article class="abs post" style="top:934px"><div class="post-title">Title E</div><div class="post-thumb">Picture E</div><p class="post-body">Lorem ipsum dosectetur adipisicing elit, sed do. Lorem ipsum dosectetur adipisicing elit, sed do. Lorem ipsum dosectetur adipisicing elit, sed do. Lorem ipsum dosectetur adipisicing elit, sed do. Lorem ipsum dosectetur adipisicing elit, sed do. Lorem ipsum dosectetur adipisicing elit, sed do. Lorem ipsum dosectetur adipisicing elit, sed do. Lorem ipsum dosectetur adipisicing elit, sed do. Lorem ipsum dosectetur adipisicing elit.</p></article>

  <aside class="abs card card-touch">
    <h3>Get in touch</h3>
    <div class="touch-art" role="img" aria-label="Illustration of a small storefront for the Circleside page"></div>
  </aside>
  <aside class="abs card card-popular">
    <h3>What’s popular?</h3>
    <div class="rank" style="top:64px">1</div>
    <div class="rank-info" style="top:62px">Lorem ipsum dolor<br>3,312,123 views</div>
    <div class="rank" style="top:108px">2</div>
    <div class="rank-info" style="top:106px">Lorem ipsum dolor<br>3,312,123 views</div>
  </aside>
  <aside class="abs card card-ambassadors">
    <h3>Ambassadors</h3>
    <div class="avatar" style="top:57px"></div>
    <div class="person" style="top:55px">John Doe<i>Young entrepreneur</i>›› Meet John</div>
    <div class="avatar" style="top:99px"></div>
    <div class="person" style="top:97px">Jane Smith<i>Pro athlete</i>›› Meet Jane</div>
    <div class="more">›› Brook-Rise ambassadors</div>
  </aside>

  <footer class="abs footer">
    <span class="copy">Copyright © 2012 brookrise. All Rights Reserved</span>
    <span class="contact">Contact : Brook Rise, Lorem street, Phone : 91-04410-553817, Email : info@brookrise.org</span>
  </footer>
</div>
</body>
</html>
```